Personal Trainer and Corporate Health Business

I need a business card for a new company I'm starting in Australia called "Brisk Vitality Partners" I will be providing a Personal training service as well as corporate health in companies.
The service provided is to help promote an active and healthy lifstyle.
The design should communicate a healthy lifestyle and also the benefits that this can have on a personal level and in the corporate environment and the benefits that flow from that.

Target Market(s)

Members of the public and Corporate

Industry/Entity Type

Environment

Requirements
Must have
• Company logo attached
Look and feel fresh and modern

Tag line: "Moving people toward better everyday wellbeing"

Lewis Norgate
Managing Director

m: 0417 596 304
e: lewis@briskvitalitypartners.com.au

www.briskvitalitypartners.com.au
Nice to have
• Can be 1 or 2 sided

```html
<!DOCTYPE html>
<html lang="en">
<head>
<meta charset="utf-8">
<title>Brisk Vitality Partners – Business Card</title>
<link rel="stylesheet" href="https://fonts.googleapis.com/css2?family=Questrial&display=swap">
<style>
  :root {
    --navy: #2f3769;
    --green: #6c9b30;
    --ink: #474a55;
    --paper: #f1f1ef;
    --white: #ffffff;
    --backdrop: #d9dadc;
  }
  * { margin: 0; padding: 0; box-sizing: border-box; }
  html, body { width: 1200px; height: 900px; overflow: hidden; }
  body {
    background: var(--backdrop);
    font-family: "Questrial", "Century Gothic", sans-serif;
    display: flex;
    flex-direction: column;
    align-items: center;
    justify-content: center;
    gap: 40px;
  }
  .card {
    width: 630px;
    height: 360px;
    position: relative;
    box-shadow: 0 6px 18px rgba(0, 0, 0, 0.18);
  }
  .card--front { background: var(--paper); }
  .card--back {
    background: var(--navy);
    display: flex;
    flex-direction: column;
    align-items: center;
    justify-content: center;
    gap: 22px;
  }
  .contact {
    position: absolute;
    left: 44px;
    top: 118px;
  }
  .contact__name {
    color: var(--navy);
    font-size: 19px;
    letter-spacing: 0.5px;
    text-transform: uppercase;
    font-weight: 400;
  }
  .contact__role {
    color: var(--green);
    font-size: 15px;
    margin-top: 2px;
    margin-bottom: 12px;
  }
  .contact__list { list-style: none; }
  .contact__item {
    display: flex;
    align-items: center;
    gap: 9px;
    color: var(--ink);
    font-size: 14px;
    line-height: 23px;
  }
  .contact__icon { width: 15px; height: 15px; flex: none; }
  .brand {
    display: flex;
    align-items: center;
    gap: 10px;
    font-size: 30px;
    letter-spacing: 1px;
    text-transform: uppercase;
  }
  .card--front .brand {
    position: absolute;
    right: 40px;
    top: 150px;
    color: var(--navy);
    flex-direction: column;
    align-items: flex-end;
    font-size: 24px;
    line-height: 1.15;
    gap: 0;
  }
  .brand__dot {
    width: 14px;
    height: 14px;
    border-radius: 50%;
    background: var(--green);
    margin-bottom: 6px;
  }
  .card--back .brand { color: var(--white); }
  .card--back .brand__dot { margin-bottom: 0; }
  .tagline {
    color: var(--green);
    font-size: 17px;
    letter-spacing: 1px;
    text-transform: uppercase;
  }
</style>
</head>
<body>
  <section class="card card--front" aria-label="Business card front">
    <div class="contact">
      <h1 class="contact__name">Lewis Norgate</h1>
      <p class="contact__role">Managing Director</p>
      <ul class="contact__list">
        <li class="contact__item">
          <svg class="contact__icon" viewBox="0 0 16 16" aria-hidden="true">
            <circle cx="8" cy="8" r="7.2" fill="none" stroke="#6c9b30" stroke-width="1.4"/>
            <rect x="5.5" y="3.8" width="5" height="8.4" rx="1" fill="none" stroke="#6c9b30" stroke-width="1.2"/>
          </svg>
          0417 596 304
        </li>
        <li class="contact__item">
          <svg class="contact__icon" viewBox="0 0 16 16" aria-hidden="true">
            <circle cx="8" cy="8" r="7.2" fill="none" stroke="#6c9b30" stroke-width="1.4"/>
            <rect x="4" y="5.3" width="8" height="5.4" fill="none" stroke="#6c9b30" stroke-width="1.1"/>
            <path d="M4 5.3 L8 8.5 L12 5.3" fill="none" stroke="#6c9b30" stroke-width="1.1"/>
          </svg>
          lewis@briskvitalitypartners.com.au
        </li>
        <li class="contact__item">
          <svg class="contact__icon" viewBox="0 0 16 16" aria-hidden="true">
            <circle cx="8" cy="8" r="7.2" fill="none" stroke="#6c9b30" stroke-width="1.4"/>
            <ellipse cx="8" cy="8" rx="2.6" ry="7" fill="none" stroke="#6c9b30" stroke-width="1"/>
            <path d="M1 8 H15 M2.2 4.6 H13.8 M2.2 11.4 H13.8" stroke="#6c9b30" stroke-width="1"/>
          </svg>
          www.briskvitalitypartners.com.au
        </li>
      </ul>
    </div>
    <div class="brand">
      <span class="brand__dot"></span>
      <span>Brisk Vitality</span>
      <span>Partners</span>
    </div>
  </section>

  <section class="card card--back" aria-label="Business card back">
    <div class="brand">
      <span class="brand__dot"></span>
      <span>Brisk Vitality Partners</span>
    </div>
    <p class="tagline">Moving people toward better everyday wellbeing</p>
  </section>
</body>
</html>
```